Vemarok Contracting Folder

Creating a design for the cover of our folders that we pass to our customers

Want to keep the same look as our colors and fonts as attached

```html
<!DOCTYPE html>
<html lang="en">
<head>
<meta charset="utf-8">
<title>Vemarok Contracting Folder Cover</title>
<link rel="stylesheet" href="https://fonts.googleapis.com/css2?family=Mulish:wght@800&family=Oranienbaum&family=Questrial&display=swap">
<style>
  :root {
    --blue: #0a32ff;
    --lavender: #abb3fb;
    --yellow: #f8d52a;
    --paper: #ffffff;
  }
  * { margin: 0; padding: 0; box-sizing: border-box; }
  html, body {
    width: 1200px;
    height: 849px;
    overflow: hidden;
    background: var(--paper);
  }
  .cover {
    position: relative;
    width: 1200px;
    height: 849px;
    background: var(--paper);
    font-family: "Questrial", sans-serif;
    color: var(--blue);
  }
  .waves {
    position: absolute;
    inset: 0;
    width: 1200px;
    height: 849px;
  }

  /* Brand block */
  .brand-square {
    position: absolute;
    left: 815px;
    top: 150px;
    width: 107px;
    height: 107px;
    background: var(--yellow);
  }
  .brand-name {
    position: absolute;
    left: 619px;
    top: 283px;
    width: 500px;
    text-align: center;
    font-family: "Oranienbaum", serif;
    font-weight: 400;
    font-size: 112px;
    line-height: 1;
    letter-spacing: 2px;
    color: var(--blue);
    transform: scaleX(0.62);
    transform-origin: center top;
    white-space: nowrap;
  }
  .brand-tagline {
    position: absolute;
    left: 686px;
    top: 382px;
    width: 366px;
    text-align: center;
    font-size: 30px;
    line-height: 1;
    letter-spacing: 2.6px;
    color: var(--lavender);
    white-space: nowrap;
  }

  /* Contact block */
  .contact {
    position: absolute;
    left: 143px;
    top: 439px;
    width: 300px;
  }
  .rule {
    position: absolute;
    left: 46px;
    width: 246px;
    height: 7px;
  }
  .rule--lavender { top: 0; background: var(--lavender); }
  .rule--yellow { top: 58px; background: var(--yellow); }
  .rule--blue { top: 186px; background: var(--blue); }
  .contact-line {
    position: absolute;
    left: 0;
    display: flex;
    align-items: baseline;
    white-space: nowrap;
    line-height: 1;
  }
  .contact-line--address { top: 20px; }
  .contact-line--phone { top: 79px; }
  .contact-line--web { top: 114px; }
  .contact-line--mail { top: 148px; }
  .contact-label {
    font-family: "Mulish", sans-serif;
    font-weight: 800;
    font-size: 28px;
    width: 48px;
    color: var(--blue);
  }
  .contact-value {
    font-size: 26px;
    color: var(--blue);
  }
  .contact-line--address .contact-value,
  .contact-line--phone .contact-value { margin-left: -4px; }
</style>
</head>
<body>
  <main class="cover">
    <svg class="waves" viewBox="0 0 1200 849" aria-hidden="true">
      <defs>
        <linearGradient id="yellowBand" x1="0" y1="849" x2="1200" y2="336" gradientUnits="userSpaceOnUse">
          <stop offset="0" stop-color="#f8d52a"/>
          <stop offset="0.55" stop-color="#f9ea6e"/>
          <stop offset="0.85" stop-color="#f8ec7a"/>
          <stop offset="1" stop-color="#fdf8d8"/>
        </linearGradient>
      </defs>
      <path class="band band--yellow" fill="url(#yellowBand)"
            d="M0,742 L744,622 Q860,603 960,524 L1200,336 L1200,428 L960,620 Q860,697 744,710 L0,828 Z"/>
      <path class="band band--lavender" fill="#abb3fb"
            d="M0,846 L744,728 Q860,712 960,634 L1200,442 L1200,849 L0,849 Z"/>
      <path class="band band--blue" fill="#0a32ff"
            d="M0,849 L1200,794 L1200,849 Z"/>
    </svg>

    <div class="brand-square"></div>
    <h1 class="brand-name">VEMAROK</h1>
    <p class="brand-tagline">Painting &amp; Contracting</p>

    <section class="contact">
      <span class="rule rule--lavender"></span>
      <p class="contact-line contact-line--address"><span class="contact-label">A/</span><span class="contact-value">Harbor Lane, 48</span></p>
      <span class="rule rule--yellow"></span>
      <p class="contact-line contact-line--phone"><span class="contact-label">T/</span><span class="contact-value">555 018 274</span></p>
      <p class="contact-line contact-line--web"><span class="contact-label">W/</span><span class="contact-value">www.vemarok.com</span></p>
      <p class="contact-line contact-line--mail"><span class="contact-label">M/</span><span class="contact-value">info@vemarok.com</span></p>
      <span class="rule rule--blue"></span>
    </section>
  </main>
</body>
</html>
```